Landing Page and Logo for Auto-Blogging Platform

I created a platform that allows users to start a blog for their business, hobby, charity, etc. I need a landing page where users can learn about the platform, benefits of consistent blogging, SEO value, plans/pricing, etc. The landing page needs to have multiple call to action buttons encouraging the visitor to register/sign up for a free trial.

In addition to the landing page, I need a page for users to establish the settings for their blog. This page should be a fairly simple form, intended for the user to enter a few details to set up their blog:
1. Name of Blog
2. Up to 10 topics and/or keywords the blog should focus on
3. Theme: Color-scheme and logo upload for blog.

I have attached the specifications of the platform's functionality so you can better understand how it works, plans/pricing, etc.

I also need a logo for the business. The name of the platform is PostNook.

Target Market(s)

Website owners, bloggers, business owners

Industry/Entity Type

Technology, Internet, web design

Coding

Coded - Design and coding required

Number of Pages Required

2 page

Colors
0054AA
0677BA
7BADD7
CADEEF
E8F1F8
0094D4
00A9DD
6FCCEA
C7EBF8
E9F6FB

Requirements
Must have
• Eye-catching design but fairly light on content (keep it simple and brief.)
Nice to have
• Eye-catching yet simple design, clean and easy to understand what we are offering.
Should not have
• Too much “wordy” and confusing content.

```html
<!DOCTYPE html>
<html lang="en">
<head>
<meta charset="utf-8">
<title>PostNook – Automate Your Blog Posting with AI</title>
<link href="https://fonts.googleapis.com/css2?family=Raleway:wght@400;500;600&display=swap" rel="stylesheet">
<style>
:root{
  --blue:#0054AA;
  --blue-mid:#0677BA;
  --blue-soft:#7BADD7;
  --blue-pale:#CADEEF;
  --blue-ice:#E8F1F8;
  --ink:#1d1d1f;
  --text:#555b63;
  --line:#d6dbe2;
  --card:#f7f7f8;
  --white:#ffffff;
}
*{margin:0;padding:0;box-sizing:border-box}
html,body{width:1200px;height:3973px;overflow:hidden}
body{font-family:'Raleway',sans-serif;color:var(--ink);background:var(--white);position:relative}
.abs{position:absolute}
a{color:inherit;text-decoration:none}

.topbar{left:0;top:0;width:1200px;height:40px;border-bottom:1px solid var(--line);text-align:center;font-size:13px;line-height:40px;color:var(--text)}
.topbar span{color:var(--blue)}
.nav{left:0;top:40px;width:1200px;height:79px;border-bottom:1px solid var(--line)}
.brand{font-weight:600;color:var(--ink);display:flex;align-items:center;gap:10px}
.brand i{display:block;background:var(--blue);border-radius:3px}
.nav .brand{left:111px;top:22px;font-size:24px}
.nav .brand i{width:26px;height:26px}
.menu{top:28px;font-size:16px;color:#3c4047}
.menu.active{color:var(--blue);font-weight:600}
.menu.active::before{content:"";position:absolute;left:50%;top:-8px;width:5px;height:5px;margin-left:-2px;border-radius:50%;background:var(--blue)}
.search{left:1072px;top:30px}

.hero{left:0;top:119px;width:1200px;height:495px;background:linear-gradient(120deg,#f4f1ee,#ebe6e1)}
.hero h1{left:111px;top:80px;font-size:43px;font-weight:500;line-height:55px;color:var(--ink)}
.hero h1 span{color:var(--blue)}
.hero p{left:111px;top:210px;width:502px;font-size:17px;line-height:26px;color:#4b4f55}
.btn{display:inline-block;background:var(--blue);color:var(--white);border-radius:5px;font-size:15px;text-align:center}
.hero .btn{left:111px;top:357px;width:227px;height:34px;line-height:34px}
.hero-photo{left:640px;top:20px;width:460px;height:475px;border-radius:230px 230px 0 0;background:linear-gradient(180deg,#e2d6c9,#a9b4c3 60%,#6d86a8)}

.section-title{width:1200px;left:0;text-align:center;font-size:34px;font-weight:500;color:var(--blue)}
.section-sub{width:1200px;left:0;text-align:center;font-size:14.5px;line-height:24px;color:#4b4f55}

.benefit{width:288px;height:295px;background:var(--card);box-shadow:0 2px 10px rgba(0,0,0,.12);text-align:center}
.benefit > svg{position:absolute;left:94px;top:20px}
.benefit h3{position:absolute;top:160px;width:100%;font-size:20px;font-weight:500}
.benefit p{position:absolute;top:200px;left:20px;right:20px;font-size:12.5px;line-height:17px;color:var(--text)}
.round-arrow{width:50px;height:50px;border-radius:50%;background:var(--blue);display:flex;align-items:center;justify-content:center}
.benefit .round-arrow{position:absolute;left:119px;top:276px}
.benefit-note{left:0;width:1200px;top:1229px;text-align:center;font-size:16px;color:var(--ink)}
.benefit-note a{color:var(--blue);text-decoration:underline}

.about{left:0;top:1337px;width:1200px;height:478px;background:linear-gradient(115deg,#f7f7f8,#eeeff0)}
.laptop{left:111px;top:82px;width:452px;height:308px;background:linear-gradient(160deg,#2d2f48,#3d2f5a 60%,#c7c9cc 88%);border-radius:10px 10px 4px 4px}
.about h2{left:600px;top:80px;font-size:34px;font-weight:500;color:var(--blue)}
.about p{left:600px;top:136px;width:488px;font-size:14.5px;line-height:23.5px;color:#4b4f55;text-align:justify}
.about .btn{left:600px;top:349px;width:120px;height:34px;line-height:34px}

.plan{background:var(--white);border:1.5px solid #e3e5e8;border-radius:14px;text-align:center}
.plan.featured{box-shadow:0 4px 18px rgba(0,0,0,.12);border-color:#ececee}
.plan h3{position:absolute;width:100%;font-size:22px;font-weight:500}
.plan.featured h3{color:var(--blue)}
.plan .badge{position:absolute;left:50%;margin-left:-60px;width:120px;height:120px;border-radius:50%;background:var(--blue-ice);display:flex;align-items:center;justify-content:center}
.plan .price{position:absolute;width:100%;font-size:26px;font-weight:500}
.plan .price sup{font-size:11px;vertical-align:12px}
.plan .price small{font-size:12px;margin-left:6px}
.plan .cta{position:absolute;left:50%;margin-left:-99px;width:198px;height:34px;line-height:32px;border:1.5px solid var(--blue-pale);border-radius:5px;color:var(--blue-mid);font-size:14px}
.plan .detail{position:absolute;width:100%;font-size:14px;line-height:19px;color:#4b4f55}
.plan .detail span{display:block;color:var(--blue);font-size:15px}

.methods{left:0;top:2547px;width:1200px;height:460px;background:linear-gradient(115deg,#f4f4f5,#ebecee)}
.methods h2{left:111px;top:95px;font-size:34px;font-weight:500;line-height:46.5px;color:var(--blue)}
.methods ul{left:111px;top:265px;list-style:none;font-size:14.5px;line-height:20px;color:#4b4f55}
.methods li{position:relative;padding-left:29px;margin-bottom:11px}
.methods li svg{position:absolute;left:0;top:2px}
.methods-photo{left:674px;top:74px;width:413px;height:386px;border-radius:200px 200px 0 0;background:linear-gradient(180deg,#2b2426,#6fb8d4 55%,#6a6e76)}

.step{width:219px;height:191px;background:var(--card);border-radius:10px;box-shadow:0 2px 10px rgba(0,0,0,.14);text-align:center}
.step svg{position:absolute;left:50%;margin-left:-32px}
.step p{position:absolute;left:14px;right:14px;font-size:12.5px;line-height:17px;color:var(--text)}
.step-num{width:64px;height:64px;border-radius:50%;background:var(--blue);border:4px solid var(--white);box-shadow:0 0 0 2px var(--blue);color:var(--white);font-size:22px;display:flex;align-items:center;justify-content:center}

.footer{left:0;top:3678px;width:1200px;height:295px;background:var(--blue-ice)}
.footer .brand{left:113px;top:60px;font-size:34px}
.footer .brand i{width:36px;height:36px}
.footer .about-text{left:113px;top:146px;width:280px;font-size:13.5px;line-height:19.5px;color:#3c4047}
.fcol{top:52px}
.fcol h4{font-size:17.5px;font-weight:500;color:var(--blue);margin-bottom:8px}
.fcol li{list-style:none;font-size:13.5px;line-height:24px;color:#3c4047}
.pay{left:874px;top:94px;width:220px;display:grid;grid-template-columns:repeat(3,auto);justify-content:space-between;gap:10px 10px;font-size:16px;font-weight:600;color:#3c4047}
.footer .rule{left:113px;top:239px;width:975px;height:1px;background:var(--blue-soft)}
.footer .copy{left:0;top:254px;width:1200px;text-align:center;font-size:13.5px;color:#3c4047}
</style>
</head>
<body>

<div class="abs topbar"><span>Lorem ipsum dolor</span> sit amet, consectetur adipiscing elit, sed do eiusmod</div>

<header class="abs nav">
  <a class="abs brand" href="#"><i></i>PostNook</a>
  <a class="abs menu active" style="left:477px" href="#">Home</a>
  <a class="abs menu" style="left:565px" href="#">About The Platform</a>
  <a class="abs menu" style="left:755px" href="#">Benefits</a>
  <a class="abs menu" style="left:859px" href="#">SEO Value</a>
  <a class="abs menu" style="left:978px" href="#">Pricing</a>
  <svg class="abs search" width="16" height="16" viewBox="0 0 16 16" fill="none" stroke="#3c4047" stroke-width="1.8"><circle cx="6.5" cy="6.5" r="5"/><path d="M10.5 10.5L15 15"/></svg>
</header>

<section class="abs hero">
  <h1 class="abs">Automate <span>Your Blog</span><br>Posting with AI</h1>
  <p class="abs">Transform your blogging experience with our AI-powered platform that not only generates and optimizes content tailored to your audience but also continuously learns and adapts to deliver smarter insights, ensuring your voice stands out in a crowded digital landscape.</p>
  <a class="abs btn" href="#">Sign Up For A Free Trial</a>
  <div class="abs hero-photo" role="img" aria-label="Photo of a smiling man in a checked shirt holding an open laptop"></div>
</section>

<h2 class="abs section-title" style="top:692px">Our Benefits</h2>
<p class="abs section-sub" style="top:752px">Lorem ipsum dolor sit amet, consectetur adipiscing elit, sed do eiusmod tempor incididunt ut<br>labore et dolore magna aliqua. Quis ipsum suspendisse ultrices gravida. Risus commodo viverra maecenas</p>

<article class="abs benefit" style="left:111px;top:851px">
  <svg width="100" height="105" viewBox="0 0 100 105" fill="none" stroke="#0054AA" stroke-width="3" stroke-linejoin="round"><rect x="10" y="6" width="62" height="94" rx="3"/><path d="M72 10l18 4-16 74"/><path d="M41 16l14 5v11c0 9-7 14-14 17-7-3-14-8-14-17V21z"/><path d="M35 31l5 5 8-9"/><path d="M18 62l4 4 7-8M36 64h26M18 82l4 4 7-8M36 84h26"/></svg>
  <h3>Establishing Authority</h3>
  <p>Lorem ipsum dolor sit amet, consectetur adipiscing elit, sed do eiusmod tempor incididunt ut labore et dolore</p>
  <a class="round-arrow" href="#"><svg width="22" height="22" viewBox="0 0 22 22" fill="none" stroke="#fff" stroke-width="3" stroke-linecap="round" stroke-linejoin="round"><path d="M4 11h14M12 5l6 6-6 6"/></svg></a>
</article>
<article class="abs benefit" style="left:455px;top:851px">
  <svg width="100" height="105" viewBox="0 0 100 105" fill="none" stroke="#0054AA" stroke-width="3" stroke-linejoin="round"><rect x="3" y="6" width="94" height="94" rx="5"/><path d="M3 22h94"/><circle cx="12" cy="14" r="2"/><circle cx="20" cy="14" r="2"/><rect x="12" y="32" width="28" height="20"/><path d="M48 34h40M48 44h30M48 52h24M12 62h44M12 72h40M12 82h36"/><path d="M88 50l8 8-30 30-11 3 3-11z"/></svg>
  <h3>Content Marketing</h3>
  <p>Lorem ipsum dolor sit amet, consectetur adipiscing elit, sed do eiusmod tempor incididunt ut labore et dolore</p>
  <a class="round-arrow" href="#"><svg width="22" height="22" viewBox="0 0 22 22" fill="none" stroke="#fff" stroke-width="3" stroke-linecap="round" stroke-linejoin="round"><path d="M4 11h14M12 5l6 6-6 6"/></svg></a>
</article>
<article class="abs benefit" style="left:799px;top:851px">
  <svg width="100" height="105" viewBox="0 0 100 105" fill="none" stroke="#0054AA" stroke-width="3" stroke-linejoin="round" stroke-linecap="round"><circle cx="62" cy="24" r="20"/><path d="M68 16c-2-3-10-3-11 1-1 5 12 4 11 10-1 4-9 4-12 1M62 10v4M62 34v4"/><path d="M8 78l16-18c6-5 12-6 20-3l14 4c4 1 4 7-1 8l-14 0"/><path d="M40 70l22-2 22-14c5-3 10 3 5 7L64 80l-26 4-12 8"/><path d="M4 82l14 14 8-6-14-14z"/></svg>
  <h3>Cost-Effective</h3>
  <p>Lorem ipsum dolor sit amet, consectetur adipiscing elit, sed do eiusmod tempor incididunt ut labore et dolore</p>
  <a class="round-arrow" href="#"><svg width="22" height="22" viewBox="0 0 22 22" fill="none" stroke="#fff" stroke-width="3" stroke-linecap="round" stroke-linejoin="round"><path d="M4 11h14M12 5l6 6-6 6"/></svg></a>
</article>

<p class="abs benefit-note">Lorem ipsum dolor sit amet, consectetur adipiscing elit, <a href="#">sed do eiusmod</a></p>

<section class="abs about">
  <div class="abs laptop" role="img" aria-label="Laptop showing the platform's analytics dashboard"></div>
  <h2 class="abs">About The Platform</h2>
  <p class="abs">There needs to be a super-admin panel where platform owner/administrator can see users, their activity, manage user access, etc.<br>Each user will have a dashboard where they control their settings such as account information, billing, view blog posts, view blog post topics, etc. From this dashboard, the user can customize the “look and feel” of their blog including theme, hero banner, header, footer, logo, color scheme, etc.</p>
  <a class="abs btn" href="#">Learn More</a>
</section>

<h2 class="abs section-title" style="top:1895px">Pricing</h2>
<p class="abs section-sub" style="top:1955px">Lorem ipsum dolor sit amet, consectetur adipiscing elit, sed do eiusmod tempor incididunt ut<br>labore et dolore magna aliqua. Quis ipsum suspendisse ultrices gravida. Risus commodo viverra maecenas</p>

<article class="abs plan" style="left:113px;top:2091px;width:293px;height:370px">
  <h3 style="top:24px">Base</h3>
  <div class="badge" style="top:65px"><svg width="70" height="64" viewBox="0 0 70 64" fill="none" stroke="#1d1d1f" stroke-width="2.5" stroke-linejoin="round"><path d="M35 4l14 7-14 7-14-7z"/><path d="M21 11v14l14 7 14-7V11M35 18v14"/><path d="M4 34l17-9M66 34l-17-9"/><path d="M4 34l31 15 31-15v12L35 61 4 46z"/><path d="M35 49v12"/></svg></div>
  <div class="price" style="top:206px"><sup>$</sup>9.99<small>/mo</small></div>
  <a class="cta" style="top:257px" href="#">Get Started</a>
  <div class="detail" style="top:309px">1 blog post (up to 2,000 words)<span>every month</span></div>
</article>
<article class="abs plan featured" style="left:444px;top:2062px;width:312px;height:399px">
  <h3 style="top:24px">Premium</h3>
  <div class="badge" style="top:70px;width:128px;height:128px;margin-left:-64px"><svg width="66" height="66" viewBox="0 0 66 66" fill="none" stroke="#1d1d1f" stroke-width="2.5" stroke-linejoin="round" stroke-linecap="round"><path d="M60 6c-16 0-28 8-36 22l14 14c14-8 22-20 22-36z"/><circle cx="44" cy="22" r="5"/><path d="M24 28H12L4 38h14M38 42v12l-10 8V48"/><path d="M16 46c-6 2-8 8-8 12 4 0 10-2 12-8"/></svg></div>
  <div class="price" style="top:220px"><sup>$</sup>14.99<small>/mo</small></div>
  <a class="cta" style="top:274px" href="#">Get Started</a>
  <div class="detail" style="top:337px">1 blog post (up to 2,000 words)<span>every week</span></div>
</article>
<article class="abs plan" style="left:794px;top:2091px;width:293px;height:370px">
  <h3 style="top:24px">Ultimate</h3>
  <div class="badge" style="top:65px"><svg width="60" height="60" viewBox="0 0 60 60" fill="none" stroke="#1d1d1f" stroke-width="2.5" stroke-linejoin="round" stroke-linecap="round"><path d="M30 2v7M18 5l3 6M42 5l-3 6"/><path d="M16 20h28l10 10-24 26L6 30z"/><path d="M6 30h48M22 20l-4 10 12 26 12-26-4-10M18 30l12-10 12 10"/></svg></div>
  <div class="price" style="top:206px"><sup>$</sup>24.99<small>/mo</small></div>
  <a class="cta" style="top:257px" href="#">Get Started</a>
  <div class="detail" style="top:309px">1 blog post (up to 2,000 words)<span>per day plus unlimited manual</span></div>
</article>

<section class="abs methods">
  <h2 class="abs">The Blog Topics Can Be<br>Created Using Any<br>Of These Methods</h2>
  <ul class="abs">
    <li><svg width="16" height="16" viewBox="0 0 16 16" fill="none" stroke="#0054AA" stroke-width="1.6"><rect x="1" y="1" width="14" height="14" rx="1"/><path d="M4 8l3 3 5-6"/></svg>The user enters them into a table manually.</li>
    <li><svg width="16" height="16" viewBox="0 0 16 16" fill="none" stroke="#0054AA" stroke-width="1.6"><rect x="1" y="1" width="14" height="14" rx="1"/><path d="M4 8l3 3 5-6"/></svg>The user uploads a list of blog topics in CSV format.</li>
    <li><svg width="16" height="16" viewBox="0 0 16 16" fill="none" stroke="#0054AA" stroke-width="1.6"><rect x="1" y="1" width="14" height="14" rx="1"/><path d="M4 8l3 3 5-6"/></svg>AI can create the list of blog topics based on a prompt such as:<br>“ Provide a list of 52 blog topics for a handyman business’s blog.”</li>
  </ul>
  <div class="abs methods-photo" role="img" aria-label="Photo of a smiling woman with curly hair working on a laptop"></div>
</section>

<h2 class="abs section-title" style="top:3088px">How to Set Up the Auto-Blog</h2>
<p class="abs section-sub" style="top:3148px">Lorem ipsum dolor sit amet, consectetur adipiscing elit, sed do eiusmod tempor incididunt ut<br>labore et dolore magna aliqua. Quis ipsum suspendisse ultrices gravida. Risus commodo viverra maecenas</p>

<article class="abs step" style="left:111px;top:3291px">
  <svg style="top:42px" width="64" height="58" viewBox="0 0 64 58" fill="none" stroke="#0054AA" stroke-width="2.2" stroke-linejoin="round"><rect x="2" y="2" width="52" height="52" rx="3"/><path d="M2 12h52M8 20h6M18 20h6M28 20h6M38 20h6M8 28h6M18 28h6M28 28h6M8 36h6M18 36h6M8 44h6"/><path d="M58 22l4 4-24 24-7 2 2-7z"/></svg>
  <p style="top:125px">Select frequency of Automated Blog Posts (daily, weekly, or monthly)</p>
</article>
<div class="abs step-num" style="left:188px;top:3245px">01</div>

<article class="abs step" style="left:364px;top:3351px">
  <svg style="top:44px" width="64" height="58" viewBox="0 0 64 58" fill="none" stroke="#0054AA" stroke-width="2.2"><rect x="4" y="2" width="56" height="54" rx="3"/><path d="M4 12h56"/><circle cx="10" cy="7" r="1.5"/><circle cx="16" cy="7" r="1.5"/><text x="32" y="38" text-anchor="middle" font-family="Raleway, sans-serif" font-size="17" font-weight="600" fill="#0054AA" stroke="none">Blog</text><path d="M14 46h36"/></svg>
  <p style="top:126px">Name your blog</p>
</article>
<div class="abs step-num" style="left:441px;top:3527px">02</div>

<article class="abs step" style="left:615px;top:3291px">
  <svg style="top:44px" width="64" height="58" viewBox="0 0 64 58" fill="none" stroke="#0054AA" stroke-width="2.2" stroke-linejoin="round"><rect x="6" y="4" width="18" height="18" rx="2"/><rect x="32" y="4" width="18" height="18" rx="2"/><rect x="6" y="30" width="18" height="18" rx="2"/><path d="M36 14l4 4 6-8"/><path d="M38 54V36a3 3 0 016 0v8h6a4 4 0 014 4v6z"/></svg>
  <p style="top:126px">Select your blog topics (or let AI choose them for you)</p>
</article>
<div class="abs step-num" style="left:693px;top:3245px">03</div>

<article class="abs step" style="left:867px;top:3351px">
  <svg style="top:40px" width="64" height="60" viewBox="0 0 64 60" fill="none" stroke="#0054AA" stroke-width="2.2"><ellipse cx="32" cy="30" rx="28" ry="11"/><ellipse cx="32" cy="30" rx="28" ry="11" transform="rotate(60 32 30)"/><ellipse cx="32" cy="30" rx="28" ry="11" transform="rotate(-60 32 30)"/><circle cx="32" cy="30" r="12" fill="#f7f7f8"/><text x="32" y="35" text-anchor="middle" font-family="Raleway, sans-serif" font-size="13" font-weight="600" fill="#0054AA" stroke="none">AI</text></svg>
  <p style="top:126px">Go do something else and let AI do all your blogging for you!</p>
</article>
<div class="abs step-num" style="left:944px;top:3526px">04</div>

<footer class="abs footer">
  <a class="abs brand" href="#"><i></i>PostNook</a>
  <p class="abs about-text">The purpose of this platform is to allow anyone to start a blog and automate the process of creating content and posting it to the blog.</p>
  <div class="abs fcol" style="left:458px">
    <h4>Quick Links</h4>
    <ul><li>Home</li><li>About The Platform</li><li>Benefits</li><li>Pricing</li><li>SEO Values</li></ul>
  </div>
  <div class="abs fcol" style="left:668px">
    <h4>Other Links</h4>
    <ul><li>FAQs</li><li>Help Center</li><li>Terms &amp; Conditions</li><li>Privacy Policy</li><li>Sitemap</li></ul>
  </div>
  <div class="abs fcol" style="left:874px"><h4>Payment</h4></div>
  <div class="abs pay"><span>Quorvel</span><span>Dashmint</span><span>Velopane</span><span>Tindrell</span><span>Ombrixa</span></div>
  <div class="abs rule"></div>
  <p class="abs copy">Copyright © 2024 PostNook. All rights reserved.</p>
</footer>

</body>
</html>
```